Business Card Professional Clean - Lumavault

Create a business card for my company that deals with Cryptocurrencies. I have a few designs ideas that I'd like to be implemented. Thanks! I will include the logo files, and a link to the design styles that I like.

Target Market(s)

Professionals

Industry/Entity Type

Consulting

Contact Information for Business Card

Name: Mark Dunn
Title: CEO/Technical Director
Phone: (587)943-0586
E-mail: mdunn@lumavault.ca
Address: Suite 512, 208-3370 Harwood Avenue NW

Twitter: @LumaVaultHQ
Instagram: lumavaulthq

Colors
92b5d7
3276b5
33a6d7
85acd3
85cae6
0592cd

Requirements
Must have
• Some colors that match with the logo and the pictures I put in below.
• Ideally the finished product would look something like the attachments showing the color gradient I want.
Nice to have
• Please see some of the attachments I've included. This is very close to the final product that I would like to see. If someone could recreate something like those I would definitely feel pretty good about it.
• For the instagram and twitter please use the symbols/icon to represent it on the card.
Should not have
• No crazy colors and unprofessional styles. I just want clear info. Don't go outside the boundaries of the colors in the attachment and we should be good. No crazy weird fonts either.

```html
<!DOCTYPE html>
<html lang="en">
<head>
<meta charset="utf-8">
<title>Lumavault Business Card</title>
<link rel="stylesheet" href="https://fonts.googleapis.com/css2?family=Cinzel:wght@400&family=Lato:wght@300;400;700&display=swap">
<style>
  :root {
    --backdrop: #25272b;
    --card: #141a24;
    --slate: #3f4858;
    --slate-light: #56606f;
    --blue-bright: #0f63c4;
    --blue-mid: #1d56a0;
    --blue-steel: #2f5a8f;
    --blue-logo: #1f6fd0;
    --text-light: #eef1f5;
    --text-muted: #b9c1cc;
  }
  * { box-sizing: border-box; margin: 0; padding: 0; }
  html, body { width: 1200px; height: 900px; overflow: hidden; }
  body {
    background: var(--backdrop);
    font-family: "Lato", Arial, sans-serif;
    position: relative;
  }
  .card {
    position: absolute;
    width: 540px;
    height: 309px;
    background: var(--card);
    border-radius: 22px;
    overflow: hidden;
    top: 296px;
  }
  .card--contact { left: 40px; }
  .card--brand { left: 620px; }

  /* brand side */
  .edge-steps {
    position: absolute;
    top: 0; bottom: 0;
    display: flex;
    flex-direction: column;
  }
  .edge-steps span { flex: 1; display: block; }
  .edge-steps--left { left: 0; width: 30px; }
  .edge-steps--right { right: 0; width: 46px; }
  .step-1 { background: var(--blue-bright); }
  .step-2 { background: var(--blue-mid); }
  .step-3 { background: var(--blue-steel); }
  .step-4 { background: var(--slate); }

  .brand-lockup {
    position: absolute;
    left: 0; right: 0; top: 108px;
    text-align: center;
  }
  .brand-name {
    font-family: "Cinzel", Georgia, serif;
    font-weight: 400;
    font-size: 46px;
    letter-spacing: 2px;
    color: var(--blue-logo);
    display: inline-flex;
    align-items: center;
    gap: 16px;
  }
  .brand-mark {
    width: 18px; height: 18px;
    background: var(--slate-light);
    display: inline-block;
  }
  .brand-url {
    margin-top: 14px;
    font-family: "Cinzel", Georgia, serif;
    font-size: 13px;
    letter-spacing: 4px;
    color: var(--blue-logo);
  }

  /* contact side */
  .name-band {
    position: absolute;
    left: 0; right: 0; top: 26px;
    height: 34px;
    background: var(--slate);
  }
  .name-band::before {
    content: "";
    position: absolute;
    left: 0; top: 0;
    width: 12px; height: 100%;
    background: var(--blue-bright);
  }
  .person-name {
    position: absolute;
    left: 30px; top: 8px;
    font-weight: 700;
    font-size: 17px;
    color: var(--text-light);
    letter-spacing: 0.3px;
  }
  .person-title {
    position: absolute;
    left: 30px; top: 64px;
    font-weight: 300;
    font-size: 12px;
    color: var(--text-muted);
    letter-spacing: 0.4px;
  }
  .contact-logo {
    position: absolute;
    right: 40px; top: 122px;
    font-family: "Cinzel", Georgia, serif;
    font-weight: 400;
    font-size: 34px;
    color: var(--blue-logo);
    letter-spacing: 1.5px;
  }
  .lower-band {
    position: absolute;
    left: 0; right: 0; top: 190px; bottom: 14px;
    background: var(--slate);
  }
  .blue-panel {
    position: absolute;
    left: 0; top: 214px;
    width: 380px; height: 95px;
    background: var(--blue-bright);
    clip-path: polygon(0 0, 100% 0, 88% 100%, 0 100%);
  }
  .contact-row {
    position: absolute;
    display: flex;
    align-items: center;
    gap: 7px;
    font-size: 13px;
    color: var(--text-light);
    white-space: nowrap;
  }
  .contact-row svg { width: 12px; height: 12px; flex: none; }
  .row-address { left: 22px; top: 195px; }
  .row-phone { left: 22px; top: 230px; }
  .row-email { left: 180px; top: 230px; }
  .row-twitter { left: 22px; top: 262px; }
  .row-instagram { left: 180px; top: 262px; }
  .social-dot {
    width: 11px; height: 11px;
    border-radius: 50%;
    background: var(--text-light);
    flex: none;
  }
</style>
</head>
<body>

  <section class="card card--contact" aria-label="Business card, contact side">
    <div class="name-band">
      <span class="person-name">MARK DUNN</span>
    </div>
    <span class="person-title">CEO/TECHNICAL DIRECTOR</span>

    <div class="contact-logo">Lumavault</div>

    <div class="lower-band"></div>
    <div class="blue-panel"></div>

    <div class="contact-row row-address">
      <svg viewBox="0 0 12 12" aria-hidden="true"><path d="M6 0.5a3.6 3.6 0 0 0-3.6 3.6C2.4 7 6 11.5 6 11.5S9.6 7 9.6 4.1A3.6 3.6 0 0 0 6 0.5zm0 5a1.4 1.4 0 1 1 0-2.8 1.4 1.4 0 0 1 0 2.8z" fill="#eef1f5"/></svg>
      <span>Suite 512, 208-3370 Harwood Avenue NW</span>
    </div>
    <div class="contact-row row-phone">
      <svg viewBox="0 0 12 12" aria-hidden="true"><path d="M2.6 0.8l1.8 2.1-1 1.3c.7 1.5 1.9 2.7 3.4 3.4l1.3-1 2.1 1.8-1 1.9C5.4 10.2 1.8 6.6 1.7 2z" fill="#eef1f5"/></svg>
      <span>(587)943-0586</span>
    </div>
    <div class="contact-row row-email">
      <svg viewBox="0 0 12 12" aria-hidden="true"><rect x="0.5" y="2" width="11" height="8" fill="#eef1f5"/><path d="M0.8 2.4L6 6.6l5.2-4.2" stroke="#0f63c4" stroke-width="1" fill="none"/></svg>
      <span>mdunn@lumavault.ca</span>
    </div>
    <div class="contact-row row-twitter">
      <span class="social-dot"></span>
      <span>@LumaVaultHQ</span>
    </div>
    <div class="contact-row row-instagram">
      <span class="social-dot"></span>
      <span>lumavaulthq</span>
    </div>
  </section>

  <section class="card card--brand" aria-label="Business card, brand side">
    <div class="edge-steps edge-steps--left">
      <span class="step-1"></span><span class="step-2"></span><span class="step-3"></span><span class="step-4"></span>
    </div>
    <div class="edge-steps edge-steps--right">
      <span class="step-1"></span><span class="step-2"></span><span class="step-3"></span><span class="step-4"></span>
    </div>
    <div class="brand-lockup">
      <div class="brand-name">Lumavault<span class="brand-mark"></span></div>
      <div class="brand-url">WWW.LUMAVAULT.CA</div>
    </div>
  </section>

</body>
</html>
```